Flyer
Zielgruppe
Wir sind eine Versicherungsmaklerfirma und benötigen einen Flyer zur Vorstellung unserer Firma bei Privatkunden und Selbstständigen.
Aufgabenstellung
Es kann das Design der Homepage aufgegriffen werden oder eigene Designvorschläge gemacht werden.
Für den Text (Inhalt) legen wir eine Word Datei bei bzw. können Informationen unserer Homepage herangezogen werden. Als Format wäre ein Falzflyer oder Din A5 gefaltet (4 Seiten) gut. Es soll Interesse für eine Beratung geweckt werden. Wenn möglich sollten 2 Beispielkunden (Musterkunde 1 Familie mit 4 Versicherungen) (Musterkunde 2 Selbstständig mit einem Firmen KFZ) eingebaut werden als Bild oder mit einem kurzen Text. und hier insbesondere eine Einsparung nach einer Beratung/Versicherungsvergleich aufgezeigt werden. Sofern genügend Platz auf dem Flyer kann auch das Maklerteam vorgestellt werden.

```html
<!DOCTYPE html>
<html lang="de">
<head>
<meta charset="utf-8">
<title>VORA Assekuranzmakler – Falzflyer</title>
<link href="https://fonts.googleapis.com/css2?family=Poppins:ital,wght@0,400;0,500;0,600;0,700;0,800;1,400&display=swap" rel="stylesheet">
<style>
:root{
  --navy:#1f2a5c;
  --navy-deep:#18214d;
  --navy-soft:#5a6390;
  --orange:#ee6f1f;
  --white:#ffffff;
  --paper:#f7f7f8;
  --ink:#1f2a5c;
  --stage:#d6d6d8;
  --photo-a:#6f7d92;
  --photo-b:#a9b3c0;
  --photo-warm:#b69a7e;
}
*{box-sizing:border-box;margin:0;padding:0}
html,body{width:803px;height:1200px;overflow:hidden;background:var(--stage);font-family:'Poppins',sans-serif;color:var(--ink)}
.spread{position:absolute;left:20px;width:763px;height:545px;background:var(--white);overflow:hidden;box-shadow:0 2px 8px rgba(0,0,0,.18)}
.spread--outside{top:35px}
.spread--inside{top:620px}
.abs{position:absolute}
.photo{position:absolute;background:linear-gradient(135deg,var(--photo-a),var(--photo-b))}
.photo--warm{background:linear-gradient(135deg,var(--photo-warm),#d9c7b2 60%,#8c7766)}
.center{text-align:center}

/* contact */
.contact{left:0;width:330px;top:32px}
.contact__title{font-size:22px;font-weight:700;color:var(--navy)}
.contact__rule{width:150px;height:2px;background:var(--orange);margin:6px auto 10px}
.icon-dot{display:block;width:14px;height:14px;margin:8px auto 3px}
.contact__phone{font-size:17px;font-weight:600}
.contact__line{font-size:13px;font-weight:500}

/* brand marks */
.brand{color:var(--navy);text-align:center;line-height:1}
.brand__name{display:block;font-weight:700;letter-spacing:1px}
.brand__sub{display:block;font-weight:700}
.brand--light{color:var(--white)}

.navy-band{position:absolute;background:var(--navy)}

/* outside right */
.welcome{left:381px;width:382px;top:303px;font-size:14.5px;font-weight:700;line-height:1.25}
.welcome em{font-style:normal;color:var(--orange)}
.tagline{left:381px;width:382px;top:343px;font-size:10px;font-style:italic;line-height:1.25}
.pill{left:445px;width:255px;top:370px;height:22px;border-radius:11px;background:var(--orange);color:var(--white);font-size:11.5px;font-weight:700;line-height:22px}
.intro{left:405px;width:335px;top:408px;color:var(--white);font-size:8.6px;line-height:1.45}
.advantage{left:381px;width:382px;top:485px;color:var(--orange);font-size:12.5px;font-weight:700}

/* inside left */
.lead{left:30px;width:330px;top:140px;font-size:10px;line-height:1.35}
.ticks{list-style:none}
.ticks li{position:relative;padding-left:17px;margin-bottom:8px;font-size:7.6px;line-height:1.35}
.ticks li::before{content:"";position:absolute;left:0;top:1px;width:10px;height:10px;border-radius:50%;background:var(--orange)}
.ticks li::after{content:"";position:absolute;left:3px;top:3.5px;width:4px;height:2.2px;border-left:1.4px solid #fff;border-bottom:1.4px solid #fff;transform:rotate(-45deg)}
.ticks b{display:block;font-size:8.2px;font-weight:700}
.benefits{left:30px;width:320px;top:182px}
.section-title{font-size:11px;font-weight:700;color:var(--navy)}
.stories-title{left:30px;top:265px}
.stories{left:30px;width:320px;top:290px;font-size:7.6px;line-height:1.4}
.why{left:30px;top:395px;color:var(--white)}
.why-rule{left:30px;top:413px;width:60px;height:1.5px;background:var(--white);opacity:.6}
.why-list{color:var(--white)}
.why-list li::before{background:var(--white)}
.why-list li::after{border-color:var(--navy)}
.why-list--a{left:30px;top:425px;width:150px}
.why-list--b{left:195px;top:425px;width:160px}

/* inside right */
.services-title{left:405px;top:28px;font-size:12px}
.services-rule{left:405px;top:47px;width:70px;height:1.5px;background:var(--navy)}
.services{left:405px;width:335px;top:58px}
.service{margin-bottom:9px}
.service__head{position:relative;padding-left:15px;font-size:8px;font-weight:700;line-height:1.3}
.service__head::before{content:"";position:absolute;left:0;top:1px;width:10px;height:10px;border-radius:50%;background:var(--orange)}
.service__head::after{content:"";position:absolute;left:3px;top:3.5px;width:4px;height:2.2px;border-left:1.4px solid #fff;border-bottom:1.4px solid #fff;transform:rotate(-45deg)}
.service ul{margin:3px 0 0 15px;padding-left:10px;font-size:7px;line-height:1.4}
.cta-box{left:395px;width:355px;top:340px;height:88px;background:var(--orange);color:var(--white);padding:10px 14px}
.cta-box h3{font-size:12px;font-weight:700;margin-bottom:9px}
.cta-box p{font-size:7px;line-height:1.45}
.appointment{left:405px;top:445px;width:170px;font-size:13px;font-weight:700;line-height:1.15}
.appointment span{color:var(--orange);display:block}
.appointment small{display:block;font-size:7px;font-weight:400;line-height:1.35;margin-top:3px;color:var(--navy)}
.footer-bar{left:381px;top:537px;width:382px;height:8px;background:var(--navy)}
</style>
</head>
<body>

<!-- Outside: back page and cover -->
<section class="spread spread--outside" aria-label="Außenseite des Flyers">
  <div class="photo" style="left:250px;top:0;width:513px;height:260px" role="img" aria-label="Foto: Berater im Anzug vor einem Bürogebäude"></div>
  <svg class="abs" style="left:0;top:0" width="763" height="545" viewBox="0 0 763 545" aria-hidden="true">
    <path d="M0,0 L255,0 C285,120 370,215 470,245 L763,250 L763,545 L0,545 Z" fill="#fff"/>
    <path d="M255,0 C285,120 370,215 470,245" fill="none" stroke="var(--orange)" stroke-width="9"/>
    <path d="M470,245 Q560,285 640,250 Q700,222 763,215 L763,240 Q700,240 645,265 Q560,300 470,245 Z" fill="var(--orange)"/>
    <path d="M440,250 Q560,300 645,262 Q700,240 763,238 L763,270 L440,270 Z" fill="#fff"/>
  </svg>

  <div class="abs contact center">
    <div class="contact__title">Kontakt</div>
    <div class="contact__rule"></div>
    <svg class="icon-dot" viewBox="0 0 14 14" aria-hidden="true"><circle cx="7" cy="7" r="7" fill="var(--orange)"/><path d="M4.5 3.8l1.6-.3.8 1.8-1 .7a5 5 0 0 0 2.1 2.1l.7-1 1.8.8-.3 1.6c-3.2.2-5.9-2.5-5.7-5.7z" fill="#fff"/></svg>
    <div class="contact__phone">+49 911 4827150</div>
    <svg class="icon-dot" viewBox="0 0 14 14" aria-hidden="true"><circle cx="7" cy="7" r="7" fill="var(--orange)"/><rect x="3.5" y="4.5" width="7" height="5" fill="none" stroke="#fff" stroke-width="1"/><path d="M3.5 4.7L7 7.4l3.5-2.7" fill="none" stroke="#fff" stroke-width="1"/></svg>
    <div class="contact__line">makler.halvesen@postfeld.org</div>
    <svg class="icon-dot" viewBox="0 0 14 14" aria-hidden="true"><circle cx="7" cy="7" r="7" fill="var(--orange)"/><circle cx="7" cy="7" r="3.6" fill="none" stroke="#fff" stroke-width="1"/><path d="M3.4 7h7.2M7 3.4c-1.8 2-1.8 5.2 0 7.2M7 3.4c1.8 2 1.8 5.2 0 7.2" fill="none" stroke="#fff" stroke-width=".8"/></svg>
    <div class="contact__line">www.vora-assekuranz.de</div>
  </div>

  <div class="photo photo--warm" style="left:0;top:240px;width:185px;height:148px" role="img" aria-label="Foto: Paar prüft Unterlagen am Tisch"></div>
  <div class="photo" style="left:194px;top:240px;width:187px;height:148px" role="img" aria-label="Foto: Berater neben einem Auto"></div>

  <div class="navy-band" style="left:0;top:395px;width:763px;height:150px"></div>
  <div class="abs brand brand--light" style="left:0;top:425px;width:381px">
    <span class="brand__name" style="font-size:74px">VORA</span>
    <span class="brand__sub" style="font-size:17px;font-weight:400;margin-top:4px">Assekuranzmakler</span>
  </div>

  <div class="abs brand" style="left:381px;top:262px;width:382px">
    <span class="brand__name" style="font-size:34px">VORA</span>
    <span class="brand__sub" style="font-size:8px;font-weight:400">Assekuranzmakler</span>
  </div>
  <div class="abs welcome center">Herzlich Willkommen bei <em>VORA</em><br>Assekuranz Versicherungsmakler!</div>
  <div class="abs tagline center">Ihr vertrauensvoller Partner für Versicherungen in<br>Nürnberg &amp; Mittelfranken</div>
  <div class="abs pill center">Persönlich. Transparent. Unabhängig.</div>
  <p class="abs intro center">Haben Sie schon einmal Ihre Versicherungsbedingungen genau durchgelesen? Wissen Sie wirklich, welche Leistungen im Schadensfall greifen – oder auch nicht? Wir helfen Ihnen dabei, Ihre Absicherung zu optimieren, unnötige Kosten zu vermeiden und gleichzeitig Ihre finanzielle Sicherheit zu stärken.</p>
  <div class="abs advantage center">Ihr Vorteil: Clever vergleichen &amp; sparen!</div>
</section>

<!-- Inside: two content pages -->
<section class="spread spread--inside" aria-label="Innenseite des Flyers">
  <div class="photo" style="left:0;top:0;width:330px;height:120px" role="img" aria-label="Foto: Beratungsgespräch mit Unterlagen und Laptop"></div>
  <svg class="abs" style="left:0;top:0" width="381" height="130" viewBox="0 0 381 130" aria-hidden="true">
    <path d="M0,110 Q160,128 260,95 Q320,70 350,0 L381,0 L381,130 L0,130 Z" fill="#fff"/>
    <path d="M0,110 Q160,128 260,95 Q320,70 350,0" fill="none" stroke="var(--orange)" stroke-width="6"/>
  </svg>
  <div class="abs brand" style="left:240px;top:92px;width:130px">
    <span class="brand__name" style="font-size:22px">VORA</span>
    <span class="brand__sub" style="font-size:6px;font-weight:400">Assekuranzmakler</span>
  </div>

  <p class="abs lead">Mit VORA Versicherungsmakler haben Sie <b>zwei<br>entscheidende Vorteile kombiniert:</b></p>
  <ul class="abs ticks benefits">
    <li><b>Günstige und leistungsstarke Produkte –</b>Dank unseres unabhängigen Versicherungsvergleichs.</li>
    <li><b>Persönliche Betreuung –</b>Wir stehen Ihnen jederzeit beratend zur Seite, insbesondere im Schadensfall.</li>
  </ul>
  <div class="abs section-title stories-title">Unsere Erfolgsgeschichten – Ihre Ersparnis!</div>
  <p class="abs stories"><b>Familie Schmidt</b> – Die klassische Familie mit 4-5 Versicherungen (z. B. Hausrat, Haftpflicht, Kfz, Unfall, Rechtsschutz) konnte durch unseren Service <b>730€ pro Jahr</b> einsparen! Firmenkunde – Ein Unternehmer optimierte mit unserer Hilfe seine KFZ Versicherung des Firmenwagens und senkte die Kosten für seinen Firmenwagen um <b>660€ jährlich.</b></p>

  <div class="navy-band" style="left:0;top:378px;width:381px;height:167px"></div>
  <div class="abs section-title why">Warum VORA Versicherungsmakler?</div>
  <div class="abs why-rule"></div>
  <ul class="abs ticks why-list why-list--a">
    <li><b>Unabhängig &amp; fair:</b>Wir sind keine Vertreter einer bestimmten Versicherung – wir arbeiten für SIE!</li>
    <li><b>Maßgeschneiderte Lösungen:</b>Jeder Kunde hat individuelle Bedürfnisse – wir finden die optimale Absicherung.</li>
  </ul>
  <ul class="abs ticks why-list why-list--b">
    <li><b>Transparente Beratung:</b>Verständlich, ehrlich und ohne versteckte Klauseln.</li>
    <li><b>100% kostenfrei:</b>Unsere Beratung kostet Sie nichts – Sie profitieren einfach von besseren Tarifen.</li>
  </ul>

  <div class="abs section-title services-title">Unsere Dienstleistungen im Überblick:</div>
  <div class="abs services-rule"></div>
  <div class="abs services">
    <div class="service">
      <div class="service__head">Versicherungs-TÜV – Wir checken Ihre bestehenden Verträge</div>
      <ul>
        <li>Passt Ihr Versicherungsschutz wirklich zu Ihrer Lebenssituation?</li>
        <li>Sind Sie möglicherweise überversichert oder zahlen zu viel?</li>
        <li>Wir überprüfen Ihre Policen und zeigen Ihnen Einsparpotenziale auf!</li>
      </ul>
    </div>
    <div class="service">
      <div class="service__head">Persönliche Beratung – Verständlich &amp; unabhängig</div>
      <ul>
        <li>Sie erhalten eine ehrliche, faire und für <b>Sie nachvollziehbare Beratung.</b></li>
        <li>Kein Fachchinesisch – wir erklären Ihnen genau, welche Leistungen für Sie sinnvoll sind. Wir zeigen Ihnen, wie Sie <b>direkt beim Versicherer „ab Werk“ einkaufen</b> – ohne teure Zwischenstationen.</li>
      </ul>
    </div>
    <div class="service">
      <div class="service__head">Betreuungskonzepte – Ganz nach Ihrem Bedarf</div>
      <ul>
        <li>Ob Sie eine intensive Betreuung oder nur gelegentliche Check-ups wünschen – wir haben das passende Konzept für Sie.</li>
      </ul>
    </div>
    <div class="service">
      <div class="service__head">Unser Versprechen: Kein Kleingedrucktes,<br>keine versteckten Kosten</div>
      <ul>
        <li>Keine zusätzlichen Gebühren – <b>unsere Beratung ist für Sie kostenfrei!</b></li>
        <li>Klare, verständliche Vertragsdetails ohne unangenehme Überraschungen.</li>
      </ul>
    </div>
  </div>

  <div class="abs cta-box">
    <h3>Jetzt beraten lassen &amp; profitieren!</h3>
    <p>Seit über 15 Jahren helfen wir Menschen in <b>Nürnberg &amp; in ganz Mittelfranken</b> dabei, ihre Versicherungen zu optimieren – insbesondere in den Bereichen <b>Krankenversicherung,</b> Berufsunfähigkeit &amp; Altersvorsorge. Lassen Sie uns gemeinsam herausfinden, wie Sie <b>mehr Leistung für weniger Geld</b> erhalten!</p>
  </div>

  <div class="abs appointment">Jetzt Termin<br>vereinbaren und<span>clever sparen!</span><small>VORA Versicherungsmakler –<br>Ihr Partner für kluge<br>Versicherungsentscheidungen.</small></div>
  <div class="abs brand" style="left:580px;top:448px;width:170px">
    <span class="brand__name" style="font-size:48px">VORA</span>
    <span class="brand__sub" style="font-size:12px;font-weight:400;margin-top:3px">Assekuranzmakler</span>
  </div>
  <div class="abs footer-bar"></div>
</section>

</body>
</html>
```